Wordpress Powered Website. Outstanding Design Required. Using Morvento Theme

Designers will not need to create anything other than the home page but there are some design elements on the home page which also need to be factored in: 6 product place holders and 2-3 slides for a slideshow (with images I provide).

Designers will need to familiarise themselves with the Morvento theme to make sure that their design will work within the theme.

The winning designer will set up all the pages and navigation in place. This includes social media icons, favicon, widgets, etc. In other words, the home page needs to be designed and coded and the other preset theme pages need to be organised in a way that we can start using the website on completion of the job.

Most of the designs I had last time were too colourful. This needs to be subtle not in your face.

Background to the business/website:
Tallow Banners is a new Australian venture which will sell large format printed banners and other signage. The market is very competitive so it is important to stand out visually and to have a website which is clean, easy to navigate and easy to order. It will be a combination of online sales and assisted sales but all sales enquiries will come from the website.

As our business is focused on presentation it is vital to have excellent design.
Purchased theme is Morvento. Only this theme is to be used.

1. A home page using all the preset features of the Morvento theme - it will just be basically taking my wireframe and inputting it to the live theme.
2. A three slide slideshow, ideally with an edited video. The static image slides can be provided by me during the handover. Placeholder for now.
Similar to this one: http://thebrindlework.com.au/

Attached is the logo which must be utilised, although it could also sit on a dark background. There is our mascot as well which can be used but does not have to be included.

Target Market(s)

Primarily B2B (business to business)
Main industries will be Construction, Retail, Community, Events & Trade Shows

Industry/Entity Type

Printing

Coding

Coded - Design and coding required

Font styles to use
Sans Serif

Requirements
Must have
• Must have the design files made to web pages within the Wordpress environment.
Nice to have
• Clean design. Stand out from competitors based on design.
Should not have
• Should not look like any competitor

```html
<!DOCTYPE html>
<html lang="en">
<head>
<meta charset="utf-8">
<title>Tallow Banners — Home</title>
<link href="https://fonts.googleapis.com/css2?family=Montserrat:wght@400;500;600;700&family=Open+Sans:wght@400;600&display=swap" rel="stylesheet">
<style>
:root{
  --topbar:#262626;
  --topbar-text:#8d8d8d;
  --header:#f4f4f4;
  --ink:#2b2b2b;
  --muted:#6b6b6b;
  --accent:#e8641e;
  --section:#f1f1f1;
  --tile-dark:#1d1d1f;
  --blue:#1f7fd6;
  --price:#e0322b;
  --gold:#d9b21c;
  --line:#d8d8d8;
}
*{box-sizing:border-box;margin:0;padding:0}
html,body{width:1200px;height:1200px;overflow:hidden}
body{position:relative;background:var(--section);font-family:"Open Sans",sans-serif;color:var(--ink)}
.abs{position:absolute}
.topbar{left:0;top:0;width:1200px;height:25px;background:var(--topbar);color:var(--topbar-text);font:400 9px "Montserrat",sans-serif}
.topbar span{position:absolute;top:8px;white-space:nowrap}
.header{left:0;top:25px;width:1200px;height:73px;background:var(--header)}
.brand{font:700 21px "Montserrat",sans-serif;color:var(--accent);display:flex;align-items:center;gap:6px;white-space:nowrap}
.brand i{display:inline-block;width:9px;height:9px;background:var(--accent);flex:none}
.header-brand{left:208px;top:17px;font-size:17px;line-height:1;align-items:flex-start;width:160px}
.header-brand i{margin-top:4px}
.header-brand span{display:block;white-space:normal;width:90px}
.nav a{position:absolute;top:33px;font:400 10px "Montserrat",sans-serif;color:var(--ink);text-decoration:none;white-space:nowrap}
.nav a.active{color:var(--accent)}
.nav .bar{position:absolute;left:385px;top:57px;width:29px;height:2px;background:var(--accent)}
.hero{left:0;top:98px;width:1200px;height:318px;background:
 radial-gradient(ellipse at 25% 30%,#6a3d5a 0%,transparent 45%),
 radial-gradient(ellipse at 60% 55%,#4a5a7a 0%,transparent 40%),
 radial-gradient(ellipse at 80% 40%,#7a6a2a 0%,transparent 35%),
 radial-gradient(ellipse at 10% 80%,#2a5a6a 0%,transparent 40%),
 radial-gradient(ellipse at 45% 90%,#7a5a20 0%,transparent 40%),
 #141218}
.hero-title{left:0;width:1200px;top:207px;text-align:center;font:500 27px "Montserrat",sans-serif;color:#c9c9c9;letter-spacing:.5px}
.hero-sub{left:0;width:1200px;top:240px;text-align:center;font:400 16px "Montserrat",sans-serif;color:#c9c9c9;letter-spacing:.5px}
.btn-ghost{left:533px;top:273px;width:134px;height:24px;border:1px solid #bdbdbd;border-radius:12px;color:#d5d5d5;font:600 8.5px "Montserrat",sans-serif;letter-spacing:1px;text-align:center;line-height:22px}
.dots{left:577px;top:377px;display:flex;gap:4px}
.dots b{width:4px;height:4px;border-radius:50%;background:#cfcfcf}
.dots b.on{background:transparent;border:1px solid #cfcfcf}
.cat-title{left:0;width:1200px;top:465px;text-align:center;font:700 21px "Montserrat",sans-serif;color:#1e1e1e}
.cat-sub{left:0;width:1200px;top:491px;text-align:center;font:400 11px "Open Sans",sans-serif;color:#333}
.cat-rule{left:500px;top:516px;width:200px;height:1px;background:#bdbdbd}
.tile{overflow:hidden}
.tile-banners{left:208px;top:545px;width:247px;height:346px;background:radial-gradient(ellipse at 60% 70%,#3a3a3c,#161618 70%)}
.tile-vinyl{left:462px;top:545px;width:275px;height:170px;background:radial-gradient(ellipse at 75% 45%,#9a7a3a,#2a3040 45%,#1c2230)}
.tile-fabric{left:462px;top:722px;width:275px;height:169px;background:radial-gradient(ellipse at 55% 55%,#6a625a,#2c3034 60%)}
.tile-murals{left:745px;top:545px;width:247px;height:346px;background:#e9e9e9}
.tag{position:absolute;left:0;top:23px;background:#e6e6e6;color:#222;font:700 11.5px "Montserrat",sans-serif;letter-spacing:.8px;padding:6px 18px 6px 8px;clip-path:polygon(0 0,100% 0,90% 100%,0 100%)}
.ban-text{left:0;width:247px;text-align:center;color:#bdbdbd}
.btn-start{left:75px;top:200px;width:98px;height:22px;border:1px solid #9a9a9a;border-radius:11px;font:600 8.5px "Montserrat",sans-serif;color:#d0d0d0;text-align:center;line-height:20px;letter-spacing:.8px}
.view-all{left:538px;top:924px;font:500 11px "Montserrat",sans-serif;color:var(--accent);letter-spacing:.8px;display:flex;align-items:center;gap:5px}
.about-title{left:208px;top:1040px;display:flex;align-items:center;gap:12px;font:400 34px "Open Sans",sans-serif;color:#1e1e1e}
.about-title .brand{font-size:26px}
.about-copy{left:208px;top:1113px;width:385px;font:400 10.5px/1.36 "Open Sans",sans-serif;color:#3a3a3a}
.about-copy p+p{margin-top:3px}
.divider-v{left:633px;top:1025px;width:1px;height:175px;background:var(--line)}
.feature-icon{left:678px;width:44px;height:56px;background:var(--gold);clip-path:polygon(0 0,100% 0,100% 100%,50% 82%,0 100%)}
.feature-title{left:744px;font:600 13px/1.2 "Montserrat",sans-serif;color:#1e1e1e}
.feature-text{left:744px;font:400 11px/1.3 "Open Sans",sans-serif;color:#555;width:250px}
.feature-rule{left:677px;top:1159px;width:315px;height:1px;background:var(--line)}
.lens{left:720px;top:313px;width:680px;height:682px;border-radius:50%;overflow:hidden;border:6px solid #fff;box-shadow:0 0 18px rgba(0,0,0,.25);background:#f7f7f7}
.lens-inner{position:absolute;left:-726px;top:-319px;width:1200px;height:1200px}
.lens-hero{left:0;top:0;width:1200px;height:416px;background:linear-gradient(100deg,#efe8ee 0%,#e8d4ec 40%,#f2eef4 100%)}
.lens-murals{left:745px;top:545px;width:260px;height:346px;background:linear-gradient(180deg,#f4f4f4,#ececec)}
.lens-murals .tag{background:#fff;color:#b5b5b5;top:25px;left:8px;font-weight:500}
.order-tab{left:879px;top:463px;width:33px;height:148px;background:var(--accent)}
.order-tab span{position:absolute;left:50%;top:50%;transform:translate(-50%,-50%) rotate(-90deg);white-space:nowrap;color:#fff;font:700 11px "Montserrat",sans-serif;letter-spacing:.6px}
.order-panel{left:912px;top:463px;width:300px;height:377px;background:#fff;box-shadow:0 2px 10px rgba(0,0,0,.12)}
.order-panel .brand{position:absolute;left:33px;top:38px;font-size:18px}
.field{position:absolute;height:26px;border:1px solid #d9d9d9;background:#fff;font:400 10px "Open Sans",sans-serif;color:#777;padding:0 10px;line-height:24px}
.field::after{content:"";position:absolute;right:8px;top:10px;border:4px solid transparent;border-top:4px solid #777}
.check{position:absolute;left:33px;top:150px;font:400 10.5px "Open Sans",sans-serif;color:#444;display:flex;align-items:center;gap:8px}
.check i{width:9px;height:9px;border:1px solid #999;background:#eee}
.price{position:absolute;left:33px;top:218px;font:400 13px "Open Sans",sans-serif;color:var(--price);white-space:nowrap}
.price sup{font-size:7px}
.price small{font-size:7.5px;color:#888;margin-left:5px}
.pill{position:absolute;left:33px;width:170px;height:21px;border-radius:11px;background:var(--blue);color:#fff;font:600 8.5px "Montserrat",sans-serif;letter-spacing:.8px;line-height:21px;padding-left:17px}
.pill::after{content:"";position:absolute;right:7px;top:6px;width:9px;height:9px;border-radius:50%;background:#fff}
.order-foot{position:absolute;left:0;top:335px;width:300px;height:42px;background:#f4f4f4;font:400 11px "Open Sans",sans-serif;color:#222;padding:14px 0 0 34px}
.order-foot u{text-underline-offset:2px}
</style>
</head>
<body>

<div class="abs topbar">
  <span style="left:207px">English ⌄</span>
  <span style="left:277px">USD ⌄</span>
  <span style="left:727px">Questions? Call ✆ 123-456-789</span>
  <span style="left:885px">User · Login / Register</span>
</div>

<header class="abs header">
  <div class="abs brand header-brand"><i></i><span>Tallow Banners</span></div>
  <nav class="nav">
    <a class="active" style="left:385px">Banners &amp; Signs</a>
    <a style="left:479px">Stands &amp; Displays</a>
    <a style="left:580px">Stickers &amp; Posters</a>
    <a style="left:681px">About Us</a>
    <a style="left:741px">Contact Us</a>
    <div class="bar"></div>
  </nav>
  <svg class="abs" style="left:814px;top:33px" width="12" height="12" viewBox="0 0 12 12"><circle cx="5" cy="5" r="3.8" fill="none" stroke="#333" stroke-width="1.6"/><path d="M8 8l3 3" stroke="#333" stroke-width="1.6"/></svg>
  <svg class="abs" style="left:860px;top:35px" width="9" height="8" viewBox="0 0 9 8"><path d="M0 1h9M0 4h9M0 7h9" stroke="#333" stroke-width="1.4"/></svg>
  <div class="abs" style="left:877px;top:33px;font:600 10px 'Montserrat',sans-serif">Cart / $2000.00</div>
  <svg class="abs" style="left:968px;top:22px" width="24" height="24" viewBox="0 0 24 24"><path d="M3 9h15l1 13H2z" fill="none" stroke="#333" stroke-width="1.8"/><path d="M7 9V6a3.5 3.5 0 017 0v3" fill="none" stroke="#333" stroke-width="1.6"/><circle cx="18" cy="6" r="5" fill="#1f7fd6"/><text x="18" y="8.5" font-size="6.5" fill="#fff" text-anchor="middle" font-family="Montserrat,sans-serif">3</text></svg>
</header>

<section class="abs hero" role="img" aria-label="Slideshow image: macro of colourful woven yarn on black"></section>
<div class="abs hero-title">Over 250 Signs &amp; Display</div>
<div class="abs hero-sub">Products in custom sizes</div>
<div class="abs btn-ghost">SEE ALL PRODUCTS</div>
<div class="abs dots"><b></b><b class="on"></b><b></b><b></b><b></b><b></b><b></b></div>

<h2 class="abs cat-title">CATEGORY</h2>
<p class="abs cat-sub">Lorem Ipsum is simply dummy text of the printing and typesetting</p>
<div class="abs cat-rule"></div>

<svg class="abs" style="left:166px;top:709px" width="22" height="18" viewBox="0 0 22 18"><path d="M21 9H2M9 1L1 9l8 8" fill="none" stroke="#444" stroke-width="1.5"/></svg>

<div class="abs tile tile-banners" role="img" aria-label="Category image: dark ink splash on black">
  <div class="abs ban-text" style="top:120px;font:600 17px 'Montserrat',sans-serif;letter-spacing:1.2px">BANNERS</div>
  <div class="abs ban-text" style="top:141px;font:400 14px 'Open Sans',sans-serif">(900MM x 600MM)</div>
  <div class="abs ban-text" style="top:160px;font:600 11px 'Montserrat',sans-serif">START AT $6.99</div>
  <div class="abs btn-start">START ORDER</div>
</div>
<div class="abs tile tile-vinyl" role="img" aria-label="Category image: cracked egg with planets on dark table"><div class="tag">VINYL STICKERS</div></div>
<div class="abs tile tile-fabric" role="img" aria-label="Category image: portrait holding a small printed card"><div class="tag">FABRIC BANNERS</div></div>
<div class="abs tile tile-murals" role="img" aria-label="Category image: wall mural with birds above a red chair"></div>

<div class="abs view-all"><svg width="9" height="9" viewBox="0 0 9 9"><circle cx="4.5" cy="4.5" r="4.5" fill="#e8641e"/><path d="M3.5 2.5l2 2-2 2" stroke="#fff" fill="none"/></svg>View All Category</div>

<div class="abs about-title">We're <span class="brand">Tallow Banners</span> !</div>
<div class="abs about-copy">
  <p>Lorem Ipsum is simply dummy text of the printing and typesetting industry.</p>
  <p>Lorem Ipsum has been the industry's standard dummy text ever since the 1500s, when an unknown printer took a galley of type and scrambled it to make a type specimen book. It has survived not only five centuries, but also the leap into electronic typesetting, remaining essentially unchanged.</p>
  <p>It was popularised in the 1960s with the release of sheets containing</p>
</div>
<div class="abs divider-v"></div>

<div class="abs feature-icon" style="top:1065px"></div>
<svg class="abs" style="left:689px;top:1073px" width="22" height="26" viewBox="0 0 22 26"><path d="M11 1l9 4v7c0 6-4 10-9 13C6 22 2 18 2 12V5z" fill="#3a3a3a"/><text x="11" y="17" font-size="11" fill="#d9b21c" text-anchor="middle" font-family="Montserrat,sans-serif">$</text></svg>
<div class="abs feature-title" style="top:1063px">100% Quality and Price<br>Guarantee</div>
<div class="abs feature-text" style="top:1099px">Lorem Ipsum is simply dummy text of the printing and typesetting industry.</div>
<div class="abs feature-rule"></div>
<div class="abs feature-icon" style="top:1196px"></div>
<div class="abs feature-title" style="top:1193px">Free Sided</div>

<div class="abs lens">
  <div class="lens-inner">
    <div class="abs lens-hero" role="img" aria-label="Faded slideshow image in soft violet tones"></div>
    <div class="abs lens-murals" role="img" aria-label="Wall mural with birds, pink blossoms and a red chair"><div class="tag">WALL MURALS</div></div>
    <div class="abs order-tab"><span>START YOUR ORDER</span></div>
    <div class="abs order-panel">
      <div class="brand"><i></i>Tallow Banners</div>
      <div class="field" style="left:33px;top:77px;width:221px">Vinyl Banners</div>
      <div class="field" style="left:33px;top:110px;width:143px">900 x 600</div>
      <div class="field" style="left:182px;top:110px;width:72px">MM</div>
      <div class="check"><i></i>Two Sided Banner</div>
      <div class="field" style="left:33px;top:174px;width:59px">01</div>
      <div class="field" style="left:98px;top:174px;width:156px">Select Shipping</div>
      <div class="price">Price: $6<sup>99</sup><small>(Incl. Shipping and Taxes)</small></div>
      <div class="pill" style="top:252px">I HAVE ARTWORK</div>
      <div class="pill" style="top:280px">I NEED DESIGN ONLINE</div>
      <div class="order-foot"><u>Quick Order</u> &nbsp;/&nbsp; <u>Request a Quote</u></div>
    </div>
  </div>
</div>

</body>
</html>
```